QRV Advisors needs a web site

We need a web site for www.qrvadvisors-example.com. QRV is a mergers and acquisition consulting company that focuses our buyer and seller services on logistics companies. We help put companies together, and help with legal and financial due diligence. We want the web site to express our service and show the logistics components. We want personalized images versus pictures of trucks and airplanes.

Our new logo uses Burgandy and grey colors. Image attached. We are not in to bold, big letters...classy, artistic, low key preferred. Confidentiality, experience, professional are what we want to express on the site.

All we expect for the first part of this project is a home page, and one subpage.  We are budgeting other funds for the technical aspects of the web site

Reason: All that I'm seeing so far is trucks, forklifts and planes. We are a legal mergers and acquisitions firm that focus on logistics. I like some of the images to say logistics, but really want it say legal, financial, and putting companies together. Will pay extra for the sub page if someone can impress us with a home page.

Reason: Swamped with another project at the moment...will work on this over the weekend and provide designer feedback and select final design by Tuesday

```html
<!DOCTYPE html>
<html lang="en">
<head>
<meta charset="utf-8">
<title>Contact Us – QRV Advisors</title>
<link href="https://fonts.googleapis.com/css2?family=Open+Sans:wght@300;400;600;700&display=swap" rel="stylesheet">
<style>
  :root {
    --crimson: #ad0039;
    --crimson-dark: #92002f;
    --crimson-deep: #7e0028;
    --ink: #4a4a4a;
    --ink-soft: #5b5b5b;
    --muted: #8a8a8a;
    --field-border: #b9b9b9;
    --page-top: #e6e6e6;
    --page-bottom: #f3f3f3;
    --footer: #2b2b2b;
    --white: #ffffff;
    --charcoal: #2f2f2f;
  }
  * { box-sizing: border-box; margin: 0; padding: 0; }
  html, body { width: 1191px; height: 1200px; overflow: hidden; }
  body {
    position: relative;
    font-family: "Open Sans", Arial, sans-serif;
    background: linear-gradient(var(--page-top), var(--page-bottom) 1021px);
    color: var(--ink);
  }
  .top-rule { position: absolute; left: 0; top: 0; width: 100%; height: 5px; background: var(--crimson); }

  /* Header */
  .brand-panel { position: absolute; left: 68px; top: 65px; width: 312px; height: 160px; }
  .brand-name {
    position: absolute; left: 84px; top: 112px;
    font-size: 30px; font-weight: 400; color: #555; letter-spacing: 1px;
    display: flex; align-items: center; gap: 10px;
  }
  .brand-mark { width: 12px; height: 12px; background: var(--crimson); display: inline-block; }

  .main-nav {
    position: absolute; left: 382px; top: 74px; width: 757px; height: 119px;
    background: linear-gradient(#b6003d, #9c0031);
    border-radius: 2px; display: flex;
    box-shadow: 0 1px 2px rgba(0,0,0,.25);
  }
  .nav-item {
    position: absolute; top: 0; height: 119px; transform: translateX(-50%);
    display: flex; flex-direction: column; align-items: center;
    color: var(--white); font-size: 16px; letter-spacing: .5px; text-decoration: none;
  }
  .nav-item svg { margin-top: 28px; height: 32px; }
  .nav-item span { position: absolute; top: 76px; white-space: nowrap; }
  .nav-item.is-active { background: var(--crimson-deep); width: 95px; }

  /* Content */
  .page-title {
    position: absolute; left: 95px; top: 268px;
    font-size: 24px; font-weight: 300; letter-spacing: 2px; color: var(--ink-soft);
  }
  .intro {
    position: absolute; left: 97px; top: 319px; width: 470px;
    font-size: 14px; line-height: 25.5px; letter-spacing: .4px; color: var(--ink);
  }
  .field {
    position: absolute; background: var(--white); border: 1px solid var(--field-border);
    border-radius: 2px; box-shadow: inset 0 1px 2px rgba(0,0,0,.08);
    font-size: 14px; color: var(--muted); letter-spacing: .4px; padding: 10px 13px;
  }
  .btn {
    position: absolute; height: 42px; border-radius: 2px; color: var(--white);
    font-size: 14.5px; letter-spacing: .5px; display: flex; align-items: center; justify-content: center;
  }
  .btn-primary { background: linear-gradient(#b8003f, #8f002e); }
  .btn-dark { background: linear-gradient(#4a4a4a, #262626); }

  /* Location */
  .map-frame {
    position: absolute; left: 621px; top: 326px; width: 499px; height: 399px;
    border: 3px solid #bdbdbd;
    background: linear-gradient(135deg, #e9e2cf, #ddd6c2 55%, #d3dccb);
  }
  .info-window {
    position: absolute; left: 646px; top: 371px; width: 229px; height: 326px;
    background: var(--white); box-shadow: 0 1px 4px rgba(0,0,0,.25);
  }
  .info-tail { position: absolute; left: 874px; top: 512px; }
  .info-title { position: absolute; left: 23px; top: 16px; font-size: 20px; font-weight: 400; color: #6a6a6a; }
  .info-rule { position: absolute; left: 23px; right: 23px; top: 57px; border-top: 1px solid #dcdcdc; }
  .info-address { position: absolute; left: 24px; top: 66px; font-size: 12.5px; line-height: 19.2px; color: #444; }
  .info-address a { color: var(--crimson); text-decoration: none; }
  .info-label { position: absolute; left: 24px; top: 164px; font-size: 13.5px; font-weight: 700; color: #8a8a8a; }
  .info-field {
    position: absolute; left: 24px; width: 180px; height: 27px; background: #f1f1f1;
    border: 1px solid #dedede; font-size: 12px; font-style: italic; color: #a0a0a0; padding: 5px 8px;
  }
  .info-btn {
    position: absolute; left: 23px; top: 269px; width: 124px; height: 27px;
    background: linear-gradient(#b8003f, #8f002e); color: var(--white);
    font-size: 12px; display: flex; align-items: center; justify-content: center; border-radius: 2px;
  }
  .info-close {
    position: absolute; left: 204px; top: 9px; width: 15px; height: 15px; border-radius: 50%;
    background: var(--crimson); color: var(--white); font-size: 10px; line-height: 14px; text-align: center;
  }

  /* Footer */
  .newsletter-band { position: absolute; left: 0; top: 1021px; width: 100%; height: 133px; background: var(--footer); }
  .newsletter-label { position: absolute; left: 166px; top: 1072px; color: var(--white); font-size: 18.5px; letter-spacing: 1px; }
  .newsletter-input {
    position: absolute; left: 496px; top: 1067px; width: 409px; height: 37px; background: var(--white);
    border-radius: 2px; font-size: 14px; color: var(--muted); letter-spacing: .4px; padding: 8px 13px;
  }
  .newsletter-btn {
    position: absolute; left: 918px; top: 1067px; width: 105px; height: 37px; border-radius: 2px;
    background: linear-gradient(#b8003f, #8f002e); color: var(--white); font-size: 13px; letter-spacing: .5px;
    display: flex; align-items: center; justify-content: center;
  }
  .legal-bar { position: absolute; left: 0; top: 1154px; width: 100%; height: 46px; background: var(--crimson); }
  .legal-text { position: absolute; left: 170px; top: 1170px; color: var(--white); font-size: 13px; letter-spacing: .4px; }
  .social-links { position: absolute; left: 923px; top: 1162px; display: flex; gap: 10px; }
  .social-links span { width: 24px; height: 24px; border-radius: 50%; background: var(--white); }
</style>
</head>
<body>
  <div class="top-rule"></div>

  <header>
    <svg class="brand-panel" viewBox="0 0 312 160" aria-hidden="true">
      <defs>
        <linearGradient id="panelFill" x1="0" y1="0" x2="0" y2="1">
          <stop offset="0" stop-color="#f7f7f7"/>
          <stop offset="1" stop-color="#cfcfcf"/>
        </linearGradient>
        <radialGradient id="panelShadow" cx="0.5" cy="0.5" r="0.5">
          <stop offset="0" stop-color="#000" stop-opacity=".22"/>
          <stop offset="1" stop-color="#000" stop-opacity="0"/>
        </radialGradient>
      </defs>
      <ellipse cx="120" cy="140" rx="110" ry="10" fill="url(#panelShadow)"/>
      <polygon points="0,0 309,0 255,135 2,135" fill="url(#panelFill)" stroke="#bdbdbd" stroke-width="1"/>
    </svg>
    <div class="brand-name"><span class="brand-mark"></span>QRV Advisors</div>

    <nav class="main-nav">
      <a class="nav-item is-active" style="left:49px">
        <svg viewBox="0 0 36 32" width="36"><path d="M18 2 L2 16 h5 v14 h8 v-9 h6 v9 h8 V16 h5 Z" fill="none" stroke="#fff" stroke-width="3" stroke-linejoin="round"/></svg>
        <span>HOME</span>
      </a>
      <a class="nav-item" style="left:181px">
        <svg viewBox="0 0 34 32" width="34"><path d="M4 10 h8 a4 4 0 1 1 8 0 h8 v8 a4 4 0 1 0 0 8 v4 H4 Z" fill="#fff"/></svg>
        <span>SERVICES &#9662;</span>
      </a>
      <a class="nav-item" style="left:337px">
        <svg viewBox="0 0 36 32" width="36" fill="none" stroke="#fff" stroke-width="2.4" stroke-linejoin="round"><path d="M18 3 L33 10 L18 17 L3 10 Z" fill="#fff"/><path d="M3 16 L18 23 L33 16"/><path d="M3 22 L18 29 L33 22"/></svg>
        <span>NEWSLETTERS</span>
      </a>
      <a class="nav-item" style="left:501px">
        <svg viewBox="0 0 48 32" width="48" fill="#fff"><circle cx="12" cy="11" r="5"/><circle cx="36" cy="11" r="5"/><circle cx="24" cy="9" r="6"/><path d="M3 28 c0-7 4-10 9-10 s9 3 9 10 Z"/><path d="M27 28 c0-7 4-10 9-10 s9 3 9 10 Z"/><path d="M13 30 c0-8 5-12 11-12 s11 4 11 12 Z"/></svg>
        <span>ABOUT US</span>
      </a>
      <a class="nav-item" style="left:657px">
        <svg viewBox="0 0 34 32" width="34"><rect x="2" y="8" width="30" height="20" fill="#fff"/><path d="M2 8 L17 20 L32 8" fill="none" stroke="#a80038" stroke-width="2"/></svg>
        <span>CONTACT US</span>
      </a>
    </nav>
  </header>

  <main>
    <h1 class="page-title">CONTACT US</h1>
    <p class="intro">Lorem ipsum dolor sit amet, consectetur adipiscing elit. Nam a risus sed justo ullamcorper commodo. Vivamus iaculis purus id ipsum laoreet, sed fermentum mauris posuere.</p>

    <form class="contact-form">
      <div class="field" style="left:98px;top:425px;width:230px;height:39px">Firstname</div>
      <div class="field" style="left:338px;top:425px;width:230px;height:39px">Email Address</div>
      <div class="field" style="left:98px;top:478px;width:230px;height:39px">Contact Number</div>
      <div class="field" style="left:338px;top:478px;width:230px;height:39px">Subject</div>
      <div class="field" style="left:98px;top:531px;width:470px;height:192px">Message</div>
      <div class="btn btn-primary" style="left:98px;top:740px;width:157px">Send Message</div>
      <div class="btn btn-dark" style="left:266px;top:740px;width:157px">Reset Form</div>
    </form>

    <div class="map-frame" role="img" aria-label="Street map showing the QRV Advisors office location"></div>
    <svg class="info-tail" width="32" height="52" viewBox="0 0 32 52" aria-hidden="true"><path d="M0 0 L30 26 L0 52 Z" fill="#fff"/></svg>
    <section class="info-window">
      <div class="info-close">&#215;</div>
      <h2 class="info-title">QRV Office</h2>
      <div class="info-rule"></div>
      <p class="info-address">1 Lorem Ipsum<br>4800 Harbor Line Avenue<br>Springfield, ST 00000<br>555-010-2040<br><a>http://qrvadvisors-example.com</a></p>
      <div class="info-label">Directions</div>
      <div class="info-field" style="top:194px">From:</div>
      <div class="info-field" style="top:227px">To:</div>
      <div class="info-btn">Get Directions</div>
    </section>
  </main>

  <footer>
    <div class="newsletter-band"></div>
    <div class="newsletter-label">SUBSCRIBE TO OUR NEWSLETTER:</div>
    <div class="newsletter-input">Email Address</div>
    <div class="newsletter-btn">SUBSCRIBE</div>
    <div class="legal-bar"></div>
    <div class="legal-text">QRV Advisors All Rights Reserved &#174; 2014</div>
    <div class="social-links" aria-label="Social links"><span></span><span></span><span></span></div>
  </footer>
</body>
</html>
```